Halvercott Orthodontics business card

Using our existing logo (created with ArtFolio), please create a tasteful, contemporary business card. We are father and daughter orthodontists specializing in braces, clarafit, etc to design healthy, beautiful smiles for children, adolescents, and adults. We would like the design to be family-friendly but not childish.
The final design should include all of the information without looking cluttered (I hope! If necessary to achieve an optimal design, please consider making the card double-sided)
Purple, black, silver on a white card
Please include the following information:
Halvercott Orthodontics (logo)
Marguerite L. Halvercott, DMD
Douglas R. Halvercott, DMD

312 Bramblewood Street
North Andover, MA 01899
978.555.0142

847C Quarry Hollow Street
Methuen, MA 01898
978.555.0187

email frontdesk@halvercottortho.example
website www.halvercottortho.example

```html
<!DOCTYPE html>
<html lang="en">
<head>
<meta charset="utf-8">
<title>Halvercott Orthodontics — Business Card</title>
<link rel="stylesheet" href="https://fonts.googleapis.com/css2?family=Libre+Baskerville:wght@400;700&family=Arimo:wght@400&display=swap">
<style>
  :root {
    --backdrop: #e6e6e4;
    --card-white: #f7f7f6;
    --card-black: #2b2b2b;
    --purple: #632d91;
    --ink: #4a4a4a;
    --rule: #8a8a8a;
    --silver: #f1f1f1;
  }
  * { box-sizing: border-box; margin: 0; padding: 0; }
  html, body {
    width: 1200px; height: 801px; overflow: hidden;
    background: var(--backdrop);
  }
  .canvas {
    position: relative; width: 1200px; height: 801px;
    display: flex; align-items: center; justify-content: center; gap: 40px;
  }
  .card {
    position: relative; width: 540px; height: 309px;
    box-shadow: 0 10px 24px rgba(0,0,0,.18);
    overflow: hidden;
  }
  /* Front */
  .card--front {
    background: var(--card-white);
    border-bottom: 4px solid var(--purple);
    font-family: "Arimo", Arial, sans-serif;
    color: var(--ink);
  }
  .brand-name {
    position: absolute; left: 30px; top: 60px;
    font-family: "Libre Baskerville", Georgia, serif;
    font-weight: 700; font-size: 21px; color: var(--purple);
    letter-spacing: .5px;
  }
  .doctor-band {
    position: absolute; right: 0; top: 0;
    width: 230px; height: 58px;
    background: var(--purple); color: #fff;
    font-family: "Libre Baskerville", Georgia, serif;
    font-weight: 700; font-size: 12.5px; line-height: 1.35;
    display: flex; flex-direction: column; justify-content: center;
    padding-left: 14px;
  }
  .offices {
    position: absolute; left: 30px; right: 30px; top: 140px;
    display: flex; justify-content: space-between;
    font-size: 14px; line-height: 1.4;
  }
  .office--right { text-align: right; }
  .phone { display: inline-flex; align-items: center; gap: 6px; }
  .icon { width: 12px; height: 12px; fill: var(--purple); flex: none; }
  .divider {
    position: absolute; left: 30px; right: 30px; top: 222px;
    height: 1px; background: var(--rule);
  }
  .web-contacts {
    position: absolute; left: 30px; right: 30px; top: 236px;
    display: flex; justify-content: space-between;
    font-size: 14px;
  }
  .web-contacts span { display: inline-flex; align-items: center; gap: 7px; }
  /* Back */
  .card--back {
    background: var(--card-black);
    display: flex; align-items: center; justify-content: flex-end;
    padding-right: 34px;
  }
  .back-brand {
    font-family: "Libre Baskerville", Georgia, serif;
    font-weight: 700; font-size: 22px; color: var(--silver);
    letter-spacing: .5px;
  }
</style>
</head>
<body>
<main class="canvas">
  <section class="card card--front" aria-label="Business card front">
    <div class="brand-name">Halvercott Orthodontics</div>
    <div class="doctor-band">
      <span>Marguerite L. Halvercott, DMD</span>
      <span>Douglas R. Halvercott, DMD</span>
    </div>
    <div class="offices">
      <address class="office office--left" style="font-style:normal">
        847C Quarry Hollow Street<br>
        Methuen, MA 01898<br>
        <span class="phone"><svg class="icon" viewBox="0 0 24 24"><path d="M6.6 10.8a15 15 0 0 0 6.6 6.6l2.2-2.2c.3-.3.7-.4 1-.2 1.1.4 2.3.6 3.6.6.6 0 1 .4 1 1V20c0 .6-.4 1-1 1A17 17 0 0 1 3 4c0-.6.4-1 1-1h3.5c.6 0 1 .4 1 1 0 1.3.2 2.5.6 3.6.1.3 0 .7-.2 1z"/></svg>978.555.0187</span>
      </address>
      <address class="office office--right" style="font-style:normal">
        312 Bramblewood Street<br>
        North Andover, MA 01899<br>
        <span class="phone"><svg class="icon" viewBox="0 0 24 24"><path d="M6.6 10.8a15 15 0 0 0 6.6 6.6l2.2-2.2c.3-.3.7-.4 1-.2 1.1.4 2.3.6 3.6.6.6 0 1 .4 1 1V20c0 .6-.4 1-1 1A17 17 0 0 1 3 4c0-.6.4-1 1-1h3.5c.6 0 1 .4 1 1 0 1.3.2 2.5.6 3.6.1.3 0 .7-.2 1z"/></svg>978.555.0142</span>
      </address>
    </div>
    <div class="divider"></div>
    <div class="web-contacts">
      <span><svg class="icon" viewBox="0 0 24 24"><path d="M2 5h20v14H2zm2 2v.5l8 5 8-5V7zm0 2.8V17h16V9.8l-8 5z"/></svg>frontdesk@halvercottortho.example</span>
      <span><svg class="icon" viewBox="0 0 24 24"><circle cx="12" cy="12" r="10"/><path d="M2 12h20M12 2c3 3 3 17 0 20M12 2c-3 3-3 17 0 20" stroke="#fff" stroke-width="1.2" fill="none"/></svg>www.halvercottortho.example</span>
    </div>
  </section>

  <section class="card card--back" aria-label="Business card back">
    <div class="back-brand">Halvercott Orthodontics</div>
  </section>
</main>
</body>
</html>
```